Redesign of Medical App for Patients

• The Designer’s task is to provide a new fully-responsive design for our apps, and then code it using only basic html and CSS.
• Your design will be incorporated into our existing REACT native app.

Target Market(s)

Medical Patients

Industry/Entity Type

Medical

Coding

Coded - Design and coding required

Number of Pages Required

5+ page

Requirements
Must have
• Short list candidates will receive detailed briefing
Nice to have
• detailed briefing contains some of our ideas.

```html
<!DOCTYPE html>
<html lang="en">
<head>
<meta charset="utf-8">
<title>Patient App Screens</title>
<link href="https://fonts.googleapis.com/css2?family=Oswald:wght@500;600&family=Roboto:wght@400;500;700&display=swap" rel="stylesheet">
<style>
:root{
  --stage:#dfe9ef;
  --screen:#e8f2f8;
  --white:#ffffff;
  --blue:#1c7fb0;
  --blue-dark:#136a98;
  --blue-text:#1a86c4;
  --orange:#f58220;
  --ink:#1c1c1c;
  --grey:#6d6d6d;
  --green:#3cbf4a;
  --red:#e53935;
}
*{box-sizing:border-box;margin:0;padding:0}
html,body{width:1200px;height:651px;overflow:hidden}
body{background:var(--stage);font-family:"Roboto",sans-serif;position:relative}
.screen{position:absolute;top:113px;width:195px;height:423px;background:var(--screen);border-radius:22px;overflow:hidden;box-shadow:0 6px 20px rgba(0,0,0,.12)}
.screen--toc{left:118px}
.screen--about{left:374px}
.screen--pre{left:630px}
.screen--proc{left:887px}
.abs{position:absolute}
.status{top:9px;left:18px;right:14px;display:flex;justify-content:space-between;font-size:6.5px;font-weight:700;color:var(--ink)}
.status svg{display:block}
/* header */
.header{top:28px;left:10px;right:10px;height:18px;display:flex;align-items:center;justify-content:space-between}
.header__title{font-family:"Oswald",sans-serif;font-weight:600;font-size:11px;color:var(--ink);letter-spacing:.2px}
.menu-btn{width:18px;height:18px;border-radius:50%;background:var(--orange);display:flex;align-items:center;justify-content:center}
/* toc */
.brand{top:31px;left:0;right:0;display:flex;align-items:center;justify-content:center;gap:5px}
.brand__dot{width:15px;height:15px;border-radius:50%;background:var(--blue-dark)}
.brand__name{font-family:"Oswald",sans-serif;font-weight:500;font-size:15px;color:var(--blue-dark);letter-spacing:.3px}
.toc-panel{top:63px;left:0;right:0;bottom:0;background:linear-gradient(160deg,var(--blue-dark),var(--blue) 60%,#2290c2);border-radius:18px 18px 0 0}
.toc-title{top:97px;left:0;right:0;text-align:center;font-family:"Oswald",sans-serif;font-weight:500;font-size:12.5px;color:var(--white)}
.toc-rule{top:116px;left:80px;width:36px;height:2px;background:var(--white)}
.toc-item{left:28px;width:141px;height:27px;border-radius:14px;background:var(--white);display:flex;align-items:center;gap:10px;padding-left:2px;font-size:8px;font-weight:500;color:var(--ink)}
.toc-item__icon{width:23px;height:23px;border-radius:50%;background:var(--orange);display:flex;align-items:center;justify-content:center;flex:none}
.toc-item--active{background:var(--orange);color:var(--white)}
.toc-item--active .toc-item__icon{background:var(--white)}
/* about */
.about-card{top:94px;left:6px;right:6px;bottom:0;background:var(--white);border-radius:18px 18px 0 0}
.avatar{top:112px;left:63px;width:68px;height:68px}
.portrait{top:58px;left:63px;width:68px;height:68px;border-radius:50%;background:radial-gradient(circle at 50% 45%,#9a6a4f,#5b3a2a 60%,#d9d9d9 62%);border:3px solid var(--white)}
.row{left:13px;width:172px;height:26px;border-radius:13px;background:var(--white);box-shadow:0 2px 6px rgba(0,0,0,.08);display:flex;align-items:center;justify-content:space-between;padding:0 12px 0 9px;font-size:5.6px;font-weight:500;color:var(--ink)}
.row--lg{font-size:7.4px;font-weight:500}
.arrow{width:7px;height:7px;flex:none}
.q-title{top:195px;left:20px;font-size:6.3px;font-weight:500;color:var(--blue-text)}
.q-body{top:209px;left:20px;width:155px;font-size:6px;line-height:12px;color:var(--grey);text-align:justify}
/* pre */
.photo{left:13px;width:171px;border:3px solid var(--white);background:linear-gradient(135deg,#e7ebee,#b8c2cf 55%,#8d98a8)}
.tab{top:172px;width:73px;height:25px;border-radius:13px;display:flex;align-items:center;justify-content:center;font-size:6.3px;font-weight:700}
.tab--on{left:22px;background:var(--orange);color:var(--white)}
.tab--off{left:100px;background:var(--white);color:var(--blue-text);box-shadow:0 2px 6px rgba(0,0,0,.08)}
.check{left:11px;width:173px;height:26px;border-radius:13px;background:var(--white);display:flex;align-items:center;gap:10px;padding:0 12px 0 10px;font-size:6.6px;color:#333}
.check__box{width:6px;height:6px;border:1px solid #555;border-radius:1px;flex:none}
.check__label{flex:1;line-height:8px}
.check__label--small{font-size:5.4px}
.note{top:382px;left:22px;font-size:5.2px;color:var(--red);display:flex;align-items:center;gap:4px}
/* procedure */
.proc-title{top:274px;left:22px;font-size:7.4px;font-weight:500;color:var(--blue-text)}
.proc-text{left:22px;width:152px;font-size:4.6px;line-height:8.9px;color:#444;text-align:justify}
</style>
</head>
<body>

<!-- Table of contents -->
<section class="screen screen--toc">
  <div class="abs status"><span>12:00</span><svg width="28" height="6" viewBox="0 0 28 6"><rect x="0" y="4" width="1.5" height="2" fill="#222"/><rect x="2.5" y="3" width="1.5" height="3" fill="#222"/><rect x="5" y="1.5" width="1.5" height="4.5" fill="#222"/><rect x="16" y="0.5" width="11" height="5" rx="1.2" fill="none" stroke="#222" stroke-width=".7"/><rect x="17" y="1.5" width="8" height="3" fill="#222"/></svg></div>
  <div class="abs brand"><span class="brand__dot"></span><span class="brand__name">CAREGUIDE</span></div>
  <div class="abs toc-panel"></div>
  <h2 class="abs toc-title">TABLE OF CONTENTS</h2>
  <div class="abs toc-rule"></div>
  <div class="abs toc-item" style="top:142px"><span class="toc-item__icon"><svg width="11" height="11" viewBox="0 0 12 12"><circle cx="6" cy="6" r="4" fill="none" stroke="#fff" stroke-width="2.2" stroke-dasharray="2 1.2"/><circle cx="6" cy="6" r="1.5" fill="#fff"/></svg></span>ABOUT PROCEDURE</div>
  <div class="abs toc-item" style="top:178px"><span class="toc-item__icon"><svg width="10" height="11" viewBox="0 0 10 12"><circle cx="5" cy="5" r="3.2" fill="#fff"/><rect x="3.8" y="8" width="2.4" height="2.5" fill="#fff"/></svg></span>PRE-PROCEDURE</div>
  <div class="abs toc-item toc-item--active" style="top:214px"><span class="toc-item__icon"><svg width="12" height="10" viewBox="0 0 12 10"><path d="M1 1.5h4l1 1 1-1h4v7H7l-1 1-1-1H1z" fill="none" stroke="#1c7fb0" stroke-width="1.2"/><line x1="6" y1="2.5" x2="6" y2="8.5" stroke="#1c7fb0" stroke-width="1"/></svg></span>PROCEDURE</div>
  <div class="abs toc-item" style="top:250px"><span class="toc-item__icon"><svg width="11" height="11" viewBox="0 0 12 12"><circle cx="6" cy="6" r="4.3" fill="none" stroke="#fff" stroke-width="1.3"/><path d="M3.8 6l1.6 1.6 3-3" fill="none" stroke="#fff" stroke-width="1.3"/></svg></span>RECOVERY</div>
  <div class="abs toc-item" style="top:286px"><span class="toc-item__icon"><svg width="11" height="11" viewBox="0 0 12 12"><path d="M1 6.5L6 2l5 4.5H9.5V10h-7V6.5z" fill="#fff"/></svg></span>AT HOME</div>
  <div class="abs toc-item" style="top:322px"><span class="toc-item__icon"><span style="color:#fff;font-weight:700;font-size:13px">?</span></span>WHAT TO DO IF</div>
  <div class="abs toc-item" style="top:358px"><span class="toc-item__icon"><svg width="11" height="11" viewBox="0 0 12 12"><circle cx="6" cy="6" r="4.5" fill="none" stroke="#fff" stroke-width="1.1"/><circle cx="6" cy="6" r="2.5" fill="none" stroke="#fff" stroke-width="1.1"/><circle cx="6" cy="6" r=".9" fill="#fff"/></svg></span>SUCCESS</div>
</section>

<!-- About procedure -->
<section class="screen screen--about">
  <div class="abs status"><span>12:00</span><svg width="28" height="6" viewBox="0 0 28 6"><rect x="0" y="4" width="1.5" height="2" fill="#222"/><rect x="2.5" y="3" width="1.5" height="3" fill="#222"/><rect x="5" y="1.5" width="1.5" height="4.5" fill="#222"/><rect x="16" y="0.5" width="11" height="5" rx="1.2" fill="none" stroke="#222" stroke-width=".7"/><rect x="17" y="1.5" width="8" height="3" fill="#222"/></svg></div>
  <div class="abs header"><svg width="12" height="6" viewBox="0 0 12 6"><path d="M12 3H1.5M3.5 .8L1 3l2.5 2.2" fill="none" stroke="#1c7fb0" stroke-width="1.3"/></svg><span class="header__title">ABOUT PROCEDURE</span><span class="menu-btn"><svg width="8" height="6" viewBox="0 0 8 6"><path d="M0 .5h8M0 3h8M0 5.5h8" stroke="#fff" stroke-width="1"/></svg></span></div>
  <div class="abs about-card"></div>
  <div class="abs portrait" role="img" aria-label="Portrait photo of a patient"></div>
  <div class="abs row" style="top:153px">Is it too late to prevent gallbladder disease?<svg class="arrow" viewBox="0 0 8 8"><circle cx="4" cy="4" r="3.4" fill="none" stroke="#555" stroke-width=".6"/><path d="M2.3 4h3.3M4.2 2.7L5.5 4 4.2 5.3" fill="none" stroke="#555" stroke-width=".6"/></svg></div>
  <p class="abs q-title">What will happen if I don’t have this procedure?</p>
  <p class="abs q-body">If you chose not to undergo surgery – and do not adopt other solutions - it is likely that your pain will persist. There is also a chance that your pain will worsen and could even lead to infection and perforation of the gallbladder - requiring more risky emergency surgery.</p>
  <div class="abs row" style="top:293px">Are there alternative solutions?<svg class="arrow" viewBox="0 0 8 8"><circle cx="4" cy="4" r="3.4" fill="none" stroke="#555" stroke-width=".6"/><path d="M2.3 4h3.3M4.2 2.7L5.5 4 4.2 5.3" fill="none" stroke="#555" stroke-width=".6"/></svg></div>
  <div class="abs row" style="top:325px">What are the risks of this procedure?<svg class="arrow" viewBox="0 0 8 8"><circle cx="4" cy="4" r="3.4" fill="none" stroke="#555" stroke-width=".6"/><path d="M2.3 4h3.3M4.2 2.7L5.5 4 4.2 5.3" fill="none" stroke="#555" stroke-width=".6"/></svg></div>
</section>

<!-- Pre-procedure -->
<section class="screen screen--pre">
  <div class="abs status"><span>12:00</span><svg width="28" height="6" viewBox="0 0 28 6"><rect x="0" y="4" width="1.5" height="2" fill="#222"/><rect x="2.5" y="3" width="1.5" height="3" fill="#222"/><rect x="5" y="1.5" width="1.5" height="4.5" fill="#222"/><rect x="16" y="0.5" width="11" height="5" rx="1.2" fill="none" stroke="#222" stroke-width=".7"/><rect x="17" y="1.5" width="8" height="3" fill="#222"/></svg></div>
  <div class="abs header"><svg width="12" height="6" viewBox="0 0 12 6"><path d="M12 3H1.5M3.5 .8L1 3l2.5 2.2" fill="none" stroke="#1c7fb0" stroke-width="1.3"/></svg><span class="header__title">PRE-PROCEDURE</span><span class="menu-btn"><svg width="8" height="6" viewBox="0 0 8 6"><path d="M0 .5h8M0 3h8M0 5.5h8" stroke="#fff" stroke-width="1"/></svg></span></div>
  <div class="abs photo" style="top:68px;height:105px" role="img" aria-label="Photo of a patient holding her side in abdominal pain"></div>
  <div class="abs tab tab--on">WEEKS BEFORE</div>
  <div class="abs tab tab--off">DAY BEFORE</div>
  <div class="abs check" style="top:212px"><span class="check__box"></span><span class="check__label">Pre-operative appointment</span><svg class="arrow" viewBox="0 0 8 8"><circle cx="4" cy="4" r="3.4" fill="none" stroke="#555" stroke-width=".6"/><path d="M4 2.3v3.3M2.7 4.2L4 5.5 5.3 4.2" fill="none" stroke="#555" stroke-width=".6"/></svg></div>
  <div class="abs check" style="top:245px"><span class="check__box"></span><span class="check__label check__label--small">8 weeks before (or after your<br>pre-operative appointment)</span><svg class="arrow" viewBox="0 0 8 8"><circle cx="4" cy="4" r="3.4" fill="none" stroke="#555" stroke-width=".6"/><path d="M4 2.3v3.3M2.7 4.2L4 5.5 5.3 4.2" fill="none" stroke="#555" stroke-width=".6"/></svg></div>
  <div class="abs check" style="top:277px"><svg width="8" height="7" viewBox="0 0 8 7" style="flex:none"><rect x=".5" y="1" width="5.5" height="5.5" fill="none" stroke="#3cbf4a" stroke-width=".7"/><path d="M1.8 3.6l1.4 1.4L7.5.6" fill="none" stroke="#3cbf4a" stroke-width="1"/></svg><span class="check__label">6 weeks before</span><svg class="arrow" viewBox="0 0 8 8"><circle cx="4" cy="4" r="3.4" fill="none" stroke="#555" stroke-width=".6"/><path d="M4 2.3v3.3M2.7 4.2L4 5.5 5.3 4.2" fill="none" stroke="#555" stroke-width=".6"/></svg></div>
  <div class="abs check" style="top:310px"><span class="check__box"></span><span class="check__label">2 weeks before</span><svg class="arrow" viewBox="0 0 8 8"><circle cx="4" cy="4" r="3.4" fill="none" stroke="#555" stroke-width=".6"/><path d="M4 2.3v3.3M2.7 4.2L4 5.5 5.3 4.2" fill="none" stroke="#555" stroke-width=".6"/></svg></div>
  <div class="abs check" style="top:343px"><span class="check__box"></span><span class="check__label">1 week before</span><svg class="arrow" viewBox="0 0 8 8"><circle cx="4" cy="4" r="3.4" fill="none" stroke="#555" stroke-width=".6"/><path d="M4 2.3v3.3M2.7 4.2L4 5.5 5.3 4.2" fill="none" stroke="#555" stroke-width=".6"/></svg></div>
  <p class="abs note"><svg width="6" height="6" viewBox="0 0 6 6"><rect x=".4" y=".8" width="4.4" height="4.4" fill="none" stroke="#e53935" stroke-width=".6"/><path d="M1.3 2.8l1.1 1.1L5.6.5" fill="none" stroke="#e53935" stroke-width=".7"/></svg>Check when task is completed</p>
</section>

<!-- Procedure -->
<section class="screen screen--proc">
  <div class="abs status"><span>12:00</span><svg width="28" height="6" viewBox="0 0 28 6"><rect x="0" y="4" width="1.5" height="2" fill="#222"/><rect x="2.5" y="3" width="1.5" height="3" fill="#222"/><rect x="5" y="1.5" width="1.5" height="4.5" fill="#222"/><rect x="16" y="0.5" width="11" height="5" rx="1.2" fill="none" stroke="#222" stroke-width=".7"/><rect x="17" y="1.5" width="8" height="3" fill="#222"/></svg></div>
  <div class="abs header"><svg width="12" height="6" viewBox="0 0 12 6"><path d="M12 3H1.5M3.5 .8L1 3l2.5 2.2" fill="none" stroke="#1c7fb0" stroke-width="1.3"/></svg><span class="header__title">PROCEDURE</span><span class="menu-btn"><svg width="8" height="6" viewBox="0 0 8 6"><path d="M0 .5h8M0 3h8M0 5.5h8" stroke="#fff" stroke-width="1"/></svg></span></div>
  <div class="abs photo" style="top:69px;height:103px;background:linear-gradient(135deg,#3c4a66,#223a7a 50%,#8c96a8)" role="img" aria-label="Photo of a hospital recovery bay with beds and monitors"></div>
  <div class="abs row row--lg" style="top:197px;left:11px;width:173px">Preparation<svg class="arrow" viewBox="0 0 8 8"><circle cx="4" cy="4" r="3.4" fill="none" stroke="#555" stroke-width=".6"/><path d="M2.3 4h3.3M4.2 2.7L5.5 4 4.2 5.3" fill="none" stroke="#555" stroke-width=".6"/></svg></div>
  <div class="abs row row--lg" style="top:230px;left:11px;width:173px">What happens?<svg class="arrow" viewBox="0 0 8 8"><circle cx="4" cy="4" r="3.4" fill="none" stroke="#555" stroke-width=".6"/><path d="M2.3 4h3.3M4.2 2.7L5.5 4 4.2 5.3" fill="none" stroke="#555" stroke-width=".6"/></svg></div>
  <h3 class="abs proc-title">Immediately after</h3>
  <p class="abs proc-text" style="top:289px">Your anesthesiologist will wean you off general anesthesia. As you start to regain consciousness, your anesthesiologist will take the breathing tube out of your mouth when you can breathe on your own. Although you will be able to respond to commands in the operating room, you will not remember any of this. You will have a breathing mask placed over your mouth and nose to increase oxygen delivery. This will enhance your recovery, prevent infection, improve wound healing.</p>
  <p class="abs proc-text" style="top:367px">The operating room staff will transport you back to your bed. You will be covered with warm blankets as you continue your recovery from general anesthesia.</p>
</section>

</body>
</html>
```